New Postcard Design Project for home loan

The project is for home loan for business owners that do no need to have any income statements. NO W2, NO TAX RETURNS, NO PAYSTUBS , CALL /TEXT/EMAIL DELVIN OKAFOR DOKAFOR@VELTORHOMEFUND.COM 555.294.8163

GET LICENSE INFORMATION FROM WEBSITE:

Here is the information you will need to have on the mailer:

- LO Name
- LO NMLS
- Branch Name (if applicable)
- Branch NMLS (if applicable)
- Branch Address (if applicable)
- Veltor Corporation
- Veltor NMLS
- Veltor Address
- Veltor Phone Number

And since you’re going to be talking about rates, you will need the following information as well:
1. Amount of the represented loan.
2. Repayment term in years of the represented loan.
3. Prepayment terms.
4. If the advertised rate may increase, the ad must state: "Advertised rate may increase"
5. Statement: "Restrictions may apply. Programs not available in all areas."

Target Market(s)

home owners that own a business

Industry/Entity Type

Home Loan refinance

Font styles to use
Serif

Colors
59FF00
82FF00
B8FF75
E3FFCB
F4FFEA
F0912C
F2A743
F7CA91
FBE8D2
FDF5EE
EE7325
F08F49
F5BC92
FAE3D3
FDF4ED
EB3D1F
EC4F4E
F09395
F8D3D4
FCEDEE

Requirements
Must have
• Must have No W2, No Tax Returns, No Paystubs Required. Must have picture of home. Home loans for business owners without traditional tax returns. MUST HAVE LOAN DISCLOSURES.
Nice to have
• Pictures of Home loan Make the customer Call the loan officer. 555.294.8163
Should not have
• My website you can extract logo: https://www.veltorhomefund.com/delvinokafor

```html
<!DOCTYPE html>
<html lang="en">
<head>
<meta charset="utf-8">
<title>Veltor Home Loan Postcard</title>
<link href="https://fonts.googleapis.com/css2?family=Montserrat:wght@300;400;500;700;800&display=swap" rel="stylesheet">
<style>
  :root {
    --ink: #3d3d3d;
    --panel: #434343;
    --yellow: #fdbd14;
    --amber: #f8ad1c;
    --blue: #4299d3;
    --brand-blue: #1a7cc7;
    --shadow: #e0e0e0;
    --paper: #ffffff;
    --night: #000000;
  }
  * { margin: 0; padding: 0; box-sizing: border-box; }
  html, body { width: 882px; height: 1200px; overflow: hidden; background: var(--night); }
  .postcards { position: relative; width: 882px; height: 1200px; font-family: "Montserrat", Arial, sans-serif; color: var(--ink); }
  .shapes { position: absolute; inset: 0; width: 882px; height: 1200px; }
  .t { position: absolute; white-space: nowrap; }

  .brand { right: 83px; top: 88px; font-size: 43px; font-weight: 500; color: var(--brand-blue); letter-spacing: -0.5px; }
  .headline { right: 77px; top: 168px; text-align: right; font-size: 49px; font-weight: 800; line-height: 48px; color: var(--ink); }
  .headline .accent { color: var(--brand-blue); }
  .subtitle { right: 77px; top: 333px; text-align: right; font-size: 13.4px; line-height: 17px; color: var(--ink); }
  .call-label { right: 81px; top: 442px; font-size: 19px; font-weight: 500; color: var(--ink); }
  .call-number { right: 81px; top: 463px; font-size: 27px; font-weight: 800; color: var(--ink); }

  .disclosures { position: absolute; left: 31px; top: 650px; list-style: none; color: #fff; font-size: 18.3px; line-height: 26px; }
  .disclosures li { position: relative; padding-left: 23px; margin-bottom: 10px; }
  .disclosures svg { position: absolute; left: 0; top: 6px; width: 16px; height: 14px; }

  .about-title { left: 85px; top: 930px; font-size: 24px; font-weight: 700; color: var(--ink); }
  .about-text { position: absolute; left: 84px; width: 370px; font-size: 14px; line-height: 17px; color: var(--ink); }
  .about-text strong { font-weight: 700; }
  .about-text.first { top: 993px; }
  .about-text.second { top: 1060px; }

  .address-pin { position: absolute; left: 509px; top: 1055px; width: 24px; height: 32px; }
  .lo-name { left: 556px; top: 1037px; font-size: 16px; font-weight: 500; color: #fff; }
  .company-line { left: 556px; font-size: 12.5px; font-weight: 300; color: #fff; }
  .company-line.one { top: 1060px; }
  .company-line.two { top: 1077px; }
  .company-line.three { top: 1094px; }
</style>
</head>
<body>
<div class="postcards">
  <svg class="shapes" viewBox="0 0 988 1344">
    <defs>
      <linearGradient id="homeTone" x1="0" y1="0" x2="1" y2="1">
        <stop offset="0" stop-color="#6b6fa3"/>
        <stop offset="0.35" stop-color="#c99a7e"/>
        <stop offset="0.65" stop-color="#2aa6c4"/>
        <stop offset="1" stop-color="#9a6a6a"/>
      </linearGradient>
    </defs>

    <!-- front side -->
    <rect x="18" y="18" width="946" height="644" fill="var(--paper)"/>
    <polygon points="18,18 138,18 100,93 18,93" fill="var(--blue)"/>
    <polygon points="18,300 480,300 540,475 595,565 645,662 18,662" fill="var(--blue)"/>
    <polygon points="100,93 138,18 665,18 515,305 18,305 18,93" fill="var(--yellow)"/>
    <polygon points="665,18 690,18 562,228 546,228" fill="var(--shadow)"/>
    <polygon points="18,588 335,588 325,608 18,608" fill="var(--yellow)"/>
    <polygon points="18,93 395,93 535,340 405,588 18,588" fill="url(#homeTone)" role="img" aria-label="Photo of a luxury home with a lit pool at dusk"/>
    <polygon points="775,476 785,458 964,458 964,476" fill="var(--amber)"/>
    <polygon points="540,476 964,476 964,563 492,563" fill="var(--yellow)"/>
    <polygon points="632,563 964,563 964,588 645,588" fill="var(--shadow)"/>

    <!-- back side -->
    <rect x="18" y="680" width="946" height="642" fill="var(--paper)"/>
    <rect x="18" y="680" width="502" height="403" fill="var(--panel)"/>
    <polygon points="18,1037 272,1037 300,1083 18,1083" fill="var(--amber)"/>
    <polygon points="18,1083 520,1083 557,1150 505,1247 615,1247 655,1322 18,1322" fill="var(--yellow)"/>
    <polygon points="785,1125 964,1125 964,1150 770,1150" fill="var(--yellow)"/>
    <polygon points="557,1150 964,1150 964,1247 505,1247" fill="var(--panel)"/>
    <polygon points="675,1247 964,1247 964,1268 687,1268" fill="var(--shadow)"/>
    <rect x="753" y="762" width="127" height="126" fill="none" stroke="var(--ink)" stroke-width="2"/>
    <g stroke="var(--ink)" stroke-width="1.2">
      <line x1="575" y1="935" x2="881" y2="935"/>
      <line x1="575" y1="993" x2="881" y2="993"/>
      <line x1="575" y1="1048" x2="881" y2="1048"/>
    </g>
  </svg>

  <div class="t brand">Veltor</div>
  <h1 class="t headline">WE WILL<br>GIVE YOU<br><span class="accent">HOME LOAN</span></h1>
  <p class="t subtitle">home loan for business owners that do no<br>need to have any income statements</p>
  <div class="t call-label">CALL THE LOAN OFFICER</div>
  <div class="t call-number">555.294.8163</div>

  <ul class="disclosures">
    <li><svg viewBox="0 0 16 14"><path d="M1 8 L5.5 12 L15 1.5" fill="none" stroke="#fff" stroke-width="2.6"/></svg>Represented loan amount: $400,000.</li>
    <li><svg viewBox="0 0 16 14"><path d="M1 8 L5.5 12 L15 1.5" fill="none" stroke="#fff" stroke-width="2.6"/></svg>Repayment term: 30 years for the<br>represented loan.</li>
    <li><svg viewBox="0 0 16 14"><path d="M1 8 L5.5 12 L15 1.5" fill="none" stroke="#fff" stroke-width="2.6"/></svg>Prepayment terms: no penalty.</li>
    <li><svg viewBox="0 0 16 14"><path d="M1 8 L5.5 12 L15 1.5" fill="none" stroke="#fff" stroke-width="2.6"/></svg>Advertised rate may increase. Rate shown<br>is for a well-qualified borrower.</li>
    <li><svg viewBox="0 0 16 14"><path d="M1 8 L5.5 12 L15 1.5" fill="none" stroke="#fff" stroke-width="2.6"/></svg>Restrictions may apply.<br>Programs not available in all areas.</li>
  </ul>

  <h2 class="t about-title">ABOUT US</h2>
  <p class="about-text first"><strong>NO W2, NO TAX RETURNS, NO PAYSTUBS.</strong><br>Home loans for business owners without<br>traditional tax returns. Call, text or email.</p>
  <p class="about-text second">DOKAFOR@VELTORHOMEFUND.COM<br>555.294.8163</p>

  <svg class="address-pin" viewBox="0 0 24 32" aria-hidden="true">
    <path d="M12 1 C5.9 1 1 5.9 1 12 C1 20 12 31 12 31 C12 31 23 20 23 12 C23 5.9 18.1 1 12 1 Z" fill="var(--yellow)"/>
    <circle cx="12" cy="12" r="4.5" fill="var(--panel)"/>
  </svg>
  <div class="t lo-name">DELVIN OKAFOR · NMLS 1948207</div>
  <div class="t company-line one">Veltor Corporation · NMLS 38215</div>
  <div class="t company-line two">2190 Harbor Way, Suite 300, Irvine, CA</div>
  <div class="t company-line three">Office 555.294.8100</div>
</div>
</body>
</html>
```